Gemstone Jewelry Online Shop Needs a Banner Design

We need a banner design for a new gemstone Jewelry Online Shop based in the U.S. called "Lumorra". One of our selling points is "never fall out of stone". We want to express: a Party Queen doesn't need to worry whenever she may meet an embarrassing moment - a stone of jewelry falls out at a very important occasion. Please insert one of attached images. Please visit our website for more details: http://lumorra-example.com/
The banner size: 1200*628
If you think other images at our website are better, please let us know. Many thanks and looking forward to your beautiful and creative designs!

Industry/Entity Type

Jewelry

```html
<!DOCTYPE html>
<html lang="en">
<head>
<meta charset="utf-8">
<title>Lumorra – never fall out of stone</title>
<link rel="stylesheet" href="https://fonts.googleapis.com/css2?family=Fira+Sans:ital,wght@0,400;1,300&display=swap">
<style>
  :root {
    --blush-light: #fbeee9;
    --blush: #f3d6cf;
    --blush-warm: #f0d3b8;
    --rose-glow: #f6c9c4;
    --ribbon-red: #e0353b;
    --ink: #232334;
    --brand-navy: #1c1c3e;
    --white: #ffffff;
    --garnet: #9b1c1f;
    --silver: #d9d9de;
  }
  * { margin: 0; padding: 0; box-sizing: border-box; }
  html, body { width: 1200px; height: 628px; overflow: hidden; }
  body { font-family: "Fira Sans", sans-serif; }

  .banner {
    position: relative;
    width: 1200px;
    height: 628px;
    overflow: hidden;
    background:
      radial-gradient(circle at 18% 12%, var(--blush-warm) 0, transparent 28%),
      radial-gradient(circle at 78% 8%, var(--rose-glow) 0, transparent 30%),
      radial-gradient(circle at 92% 40%, var(--blush-warm) 0, transparent 22%),
      linear-gradient(180deg, var(--blush) 0%, var(--blush-light) 55%, var(--white) 100%);
  }

  .slogan {
    position: absolute;
    left: 82px;
    top: 62px;
    width: 428px;
    height: 163px;
  }
  .slogan svg { position: absolute; inset: 0; }
  .slogan-text {
    position: relative;
    padding: 18px 0 0 34px;
    color: var(--white);
    font-style: italic;
    font-weight: 300;
    font-size: 58px;
    line-height: 72px;
    letter-spacing: 0.5px;
  }

  .brand-name {
    position: absolute;
    left: 100px;
    top: 300px;
    color: var(--brand-navy);
    font-weight: 400;
    font-size: 60px;
    letter-spacing: 1px;
  }

  .pitch {
    position: absolute;
    left: 102px;
    top: 434px;
    color: var(--ink);
    font-size: 26px;
    line-height: 37px;
    white-space: nowrap;
  }

  .product-photo {
    position: absolute;
    left: 780px;
    top: 135px;
    width: 300px;
    height: 375px;
    border-radius: 46% 46% 40% 40%;
    background:
      radial-gradient(circle at 50% 36%, var(--garnet) 0, #b8292c 22%, transparent 46%),
      radial-gradient(circle at 50% 38%, #c23a3c 0, var(--silver) 62%, transparent 72%);
  }
  .product-reflection {
    position: absolute;
    left: 800px;
    top: 540px;
    width: 260px;
    height: 88px;
    border-radius: 50% 50% 0 0;
    background: linear-gradient(180deg, rgba(217,217,222,0.45), rgba(255,255,255,0));
  }
</style>
</head>
<body>
  <main class="banner">
    <div class="slogan">
      <svg width="428" height="163" viewBox="0 0 428 163" aria-hidden="true">
        <polygon points="0,0 373,0 373,68 428,68 428,163 0,163" fill="var(--ribbon-red)"/>
      </svg>
      <h1 class="slogan-text">never fall<br>out of stone</h1>
    </div>

    <div class="brand-name">Lumorra</div>

    <p class="pitch">a Party Queen doesn't need to worry whenever<br>she may meet an embarrassing moment - a stone of<br>jewelry falls out at a very important occasion.</p>

    <div class="product-photo" role="img" aria-label="Sterling silver flower ring set with an oval red garnet in a halo of small white stones, surrounded by pear-shaped garnet petals"></div>
    <div class="product-reflection" role="img" aria-label="Soft reflection of the ring on a glossy surface"></div>
  </main>
</body>
</html>
```